Website refresh! Software products and services.
B2B site: 3 page templates, Well thought out requirements, brief and some wireframes
Website refresh! Software products and services. - Information Technology
Creative Brief
Information Technology
www.qnr.co.nz
QNR is a software company focussed on Operations Management and Operations Intelligence systems for Utilities (Elec, Gas, Water), Transport/Logistics companies, and Radio network users. We have been in business for 10+ years and have clients all over the world. Our products are robust, credible, and meet the needs of these customers.
This is a B2B site. Needs to be clean and easy to navigate, information, screen shots, relevant graphics. Refer to the attached preliminary design brief.
High Tech
Red banner
Blue
Arial, Verdana, Trebuchet MS, Times New Roman, Century Gothic, Georgia
left side
www.larkmoorco.com
http://www.7jq.com
http://www.vo-powerline.com/products_and_services/products/utility_operations_software/
CMS will be wordpress. 3 page Templates and associated graphics. 1. Home/Landing page 2. Inside Category and Product Pages 3. Miscellaneous pages, eg Contact Us, Careers, News & Events, etc. Refer to the attached Summary design brief which has example sites, UI ideas, Wireframes of suggested page layout. Copy will also be provided to the selected designer so they can see how the content will fit with design.

```html
<!DOCTYPE html>
<html lang="en">
<head>
<meta charset="utf-8">
<title>QNR – Operations Management Software</title>
<link href="https://fonts.googleapis.com/css2?family=Arimo:wght@400;700&display=swap" rel="stylesheet">
<style>
:root{
  --blue:#1d4f8c;
  --blue-dark:#123a6b;
  --red:#d8232a;
  --red-dark:#a9161c;
  --ink:#333;
  --muted:#666;
  --rule:#d5d5d5;
  --panel:#f3f3f3;
  --page:#ececec;
  --white:#fff;
}
*{box-sizing:border-box;margin:0;padding:0}
html,body{width:1200px;height:1080px;overflow:hidden}
body{background:var(--page);font-family:"Arimo",Arial,sans-serif;color:var(--ink)}
.page{width:1200px;height:1080px;background:var(--white);padding:0 40px;position:relative}
.masthead{height:100px;position:relative;display:flex;align-items:center}
.brand{font-weight:700;font-size:46px;color:#222;letter-spacing:1px}
.tagline-art{position:absolute;left:380px;top:0;width:330px;height:100px;
  background:linear-gradient(90deg,#f6f6f6,#dcdcdc 50%,#f4f4f4);display:flex;align-items:flex-end;justify-content:center;gap:16px;padding-bottom:14px;
  font-size:28px;color:#8a8a8a;white-space:nowrap}
.tagline-art .strong{color:#555;font-size:34px}
.utility{position:absolute;right:40px;top:18px;display:flex;gap:14px}
.lang{border:1px solid #bbb;background:#fafafa;font-size:14px;padding:5px 10px;width:150px}
.support{background:var(--red);color:var(--white);font-size:14px;padding:6px 14px;border-radius:2px}
.mainnav{height:38px;background:linear-gradient(var(--blue),var(--blue-dark));display:flex;align-items:center;padding-left:20px;gap:40px}
.mainnav a{color:var(--white);text-decoration:none;font-size:15px}
.feature{display:flex;margin-top:14px;height:400px;gap:8px}
.slider{flex:0 0 730px;position:relative;
  background:radial-gradient(circle at 30% 30%,#6d8fc4,#2b4e8a 45%,#0f2448 90%);color:var(--white)}
.slider-copy{position:absolute;left:300px;top:150px;width:380px}
.slider-copy h2{font-size:28px;line-height:1.25;font-weight:700;margin-bottom:14px}
.slider-copy p{font-size:15px;line-height:1.4;color:#dfe7f3}
.dots{position:absolute;left:50%;bottom:14px;transform:translateX(-50%);display:flex;gap:8px}
.dots span{width:10px;height:10px;border-radius:50%;background:#9db2d4}
.dots span.on{background:var(--white)}
.solutions{flex:1;display:flex;flex-direction:column;gap:4px}
.solution{flex:1;background:var(--panel);border:1px solid #ddd;display:flex;align-items:center;justify-content:space-between;padding:0 14px;gap:10px}
.solution h3{font-size:15px;color:var(--red);font-weight:700;margin-bottom:4px}
.solution p{font-size:12px;color:var(--muted);line-height:1.3}
.solution .thumb{flex:0 0 66px;height:56px;background:linear-gradient(#ffffff,#c9ccd2);border-radius:4px}
.solution.active{background:linear-gradient(var(--red),var(--red-dark));border-color:var(--red-dark)}
.solution.active h3,.solution.active p{color:var(--white)}
.columns{display:flex;gap:30px;margin-top:24px}
.col h2{font-size:22px;font-weight:700;color:#222;padding-bottom:8px;border-bottom:3px solid var(--red);margin-bottom:18px}
.col-news{flex:0 0 370px}
.col-product{flex:0 0 400px}
.col-contact{flex:1}
.col h4{color:var(--blue);font-size:15px;margin-bottom:12px}
.col p{font-size:13px;line-height:1.45;margin-bottom:14px;color:#444}
.phones{font-size:13px;line-height:1.55;margin-bottom:16px}
.col a{color:var(--blue);font-size:13px}
.share{display:flex;align-items:center;gap:10px;margin-top:22px;font-size:13px}
.share-icon{width:32px;height:32px;border-radius:50%;background:#555;display:flex;align-items:center;justify-content:center}
.footer{position:absolute;left:40px;right:40px;top:950px;border-top:1px solid var(--rule);padding-top:12px;display:flex;justify-content:space-between;font-size:12px;color:var(--muted)}
</style>
</head>
<body>
<div class="page">
  <header class="masthead">
    <div class="brand">QNR</div>
    <div class="tagline-art" role="img" aria-label="Hand holding a tagline banner: Reliability, Innovation, Trust">
      <span>Reliability</span><span>Innovation</span><span class="strong">Trust</span>
    </div>
    <div class="utility">
      <div class="lang">Select Language ▾</div>
      <div class="support">Support Portal</div>
    </div>
  </header>

  <nav class="mainnav">
    <a href="#">Home</a><a href="#">Product Solutions</a><a href="#">Partners</a><a href="#">News &amp; Events</a><a href="#">Careers</a><a href="#">About QNR</a><a href="#">Contacts</a>
  </nav>

  <section class="feature">
    <div class="slider" role="img" aria-label="Lightning storm over a night sky">
      <div class="slider-copy">
        <h2>When the Power goes off and everyone starts phoning in...</h2>
        <p>Torrent – Fast efficient, comprehensive customer communications, less calls, more information</p>
      </div>
      <div class="dots"><span class="on"></span><span></span><span></span><span></span></div>
    </div>
    <div class="solutions">
      <div class="solution"><div><h3>TROUBLE CALL MANAGEMENT</h3><p>Integrated with SCADA, outbound communications</p></div><div class="thumb" role="img" aria-label="Telephone handset"></div></div>
      <div class="solution active"><div><h3>OUTAGE, OPERATIONS AND WORKS MANAGEMENT</h3><p>Solutions for Networks, Retailers or Contractors</p></div><div class="thumb" role="img" aria-label="Operations screen"></div></div>
      <div class="solution"><div><h3>ENTERPRISE GRADE AVL</h3><p>Multi-branded SaaS software and hardware solution for OEM, White label, and Enterprise deployment</p></div><div class="thumb" role="img" aria-label="Vehicle tracking unit"></div></div>
      <div class="solution"><div><h3>RADIO USERS</h3><p>Dispatch and AVL - MPT1327 &amp; P25 solutions</p></div><div class="thumb" role="img" aria-label="Two-way radio"></div></div>
      <div class="solution"><div><h3>TELCO SOLUTIONS</h3><p>OEM, White label, or partnered solutions for Telco's</p></div><div class="thumb" role="img" aria-label="Mobile phone"></div></div>
    </div>
  </section>

  <section class="columns">
    <div class="col col-news">
      <h2>Announcements &amp; News</h2>
      <h4>Announcing Rover 3!</h4>
      <p>QNR proudly announces the release of Rover 3 on 1 May 2007. Rover 3 represents the redevelopment of the Rover 2 and Fleetline applications bringing these together in a single solution.</p>
      <p>Rover 3 delivers Automated Vehicle Location (AVL) and job dispatch, and is ideal for organisations operating fleets of vehicles of any size. Rover brings together in-vehicle and software technology to monitor vehicle location in real-time via a GPS interface. All functional aspects, including notification, mapping and reporting are accessed via mobile radio or GPRS cellular on an easy-to-use website (Vireo Browser 6.0 or higher).</p>
    </div>
    <div class="col col-product">
      <h2>Featured Product release</h2>
      <p>Rover 3 delivers Automated Vehicle Location (AVL) and job dispatch, and is ideal for organisations operating fleets of vehicles of any size. Rover brings together in-vehicle and software technology to monitor vehicle location in real-time via a GPS interface.</p>
      <p>All functional aspects, including notification, mapping and reporting are accessed via mobile radio or GPRS cellular on an easy-to-use website (Vireo Browser 6.0 or higher).</p>
    </div>
    <div class="col col-contact">
      <h2>Contact us</h2>
      <p>Email and Phone details</p>
      <div class="phones">Europe: +44 512<br>Australia: +61 7<br>USA: +1 555 204 7716<br>Canada: +1 555<br>New Zealand: +649 555 0142</div>
      <a href="#">info@qnr.co.nz</a>
      <div class="share">
        <span class="share-icon"><svg width="18" height="14" viewBox="0 0 18 14"><rect x="1" y="1" width="16" height="12" fill="none" stroke="#fff" stroke-width="1.5"/><path d="M1 1l8 7 8-7" fill="none" stroke="#fff" stroke-width="1.5"/></svg></span>
        Email to a friend
      </div>
    </div>
  </section>

  <footer class="footer">
    <span>© 2011 QNR ™ | Legal</span>
    <span>Product Solutions | Partners | News &amp; Events | Careers | About QNR | Contacts</span>
  </footer>
</div>
</body>
</html>
```